Website Design for Law Firm

We need a fresh new website design for our client 'Torvek Legal' who specialises as a Criminal, Traffic & Civil Lawyer in Perth, Western Australia. We are looking for a very clean, professional and elegant look for the website, a presence of power and class needed as he deals with high end clients. Black, Silver and hints of gold need to run through the design without making the site look too dark. We are after a very modern, spacious web look, use of large readable text with links to social media (such as Facebook, Google+, Twitter, LinkedIn) to stand out and his contact details to be made very predominate.

Reason: Public holidays here in Australia, need more business hours to discuss designs with client.

Reason: Client needs more time to look through designs.

Reason: Client is going over last of designs. Design will be picked early next week!

Law Firm

```html
<!DOCTYPE html>
<html lang="en">
<head>
<meta charset="utf-8">
<title>Torvek Legal — Criminal, Traffic &amp; Civil Lawyer, Perth WA</title>
<link rel="stylesheet" href="https://fonts.googleapis.com/css2?family=PT+Sans:ital,wght@0,400;0,700;1,400&family=Arimo:wght@400;700&display=swap">
<style>
:root{
  --ink:#1d1d1d;
  --text:#3a3a3a;
  --muted:#8a8a8a;
  --rule:#d4d4d4;
  --paper:#ffffff;
  --band:#ececec;
  --nav:#232323;
  --footer:#231f1f;
  --footer-deep:#141212;
  --field:#3d3939;
  --button:#1f1f1f;
}
*{box-sizing:border-box;margin:0;padding:0}
html,body{width:1200px;height:2239px;overflow:hidden}
body{position:relative;background:var(--paper);font-family:"PT Sans",sans-serif;color:var(--text)}
.abs{position:absolute}
p{font-size:10px;line-height:16px}

/* header */
.site-header{left:0;top:0;width:1200px;height:68px;background:var(--paper)}
.brand{left:221px;top:18px;display:flex;align-items:center;gap:8px}
.brand-mark{width:14px;height:14px;background:var(--ink);border-radius:50%}
.brand-name{font-size:19px;font-weight:700;color:var(--ink);letter-spacing:.5px}
.header-phone{left:876px;top:28px;display:flex;align-items:center;gap:8px;font-family:"Arimo",sans-serif;font-size:11px;color:var(--ink)}

.main-nav{left:0;top:68px;width:1200px;height:45px;background:var(--nav)}
.main-nav ul{list-style:none;display:flex;justify-content:space-between;position:absolute;left:210px;width:778px;top:0;height:45px;align-items:center}
.main-nav li{font-family:"Arimo",sans-serif;font-size:10px;color:#fff;white-space:nowrap}

/* hero */
.hero{left:0;top:113px;width:1200px;height:424px;background:radial-gradient(ellipse at 45% 45%,#8a5448 0%,#5e2f2a 45%,#2b1514 100%)}
.hero-quote{left:594px;top:204px;width:448px;height:109px;background:rgba(40,24,22,.82);padding:18px 20px;color:#f3ece8;font-style:italic;font-size:17px;line-height:26px;text-align:justify}
.hero-arrow{top:239px;width:40px;height:48px;background:#f4f4f4;display:flex;align-items:center;justify-content:center}
.hero-arrow.prev{left:0}
.hero-arrow.next{right:0}

/* section headings */
.section-title{font-size:16px;font-weight:700;color:var(--ink)}
.title-rule{height:1px;background:var(--rule)}

.intro-title{left:213px;top:574px;font-size:17px}
.photo{background:linear-gradient(135deg,#5a3a22,#1e140e)}
.intro-text{left:376px;top:634px;width:611px;text-align:justify}

.band{left:0;width:1200px;background:var(--band)}
.more-btn{width:61px;height:24px;background:var(--button);color:#fff;border-radius:3px;font-size:10px;display:flex;align-items:center;justify-content:center}

.scope-list{list-style:none;left:624px;top:928px;width:362px}
.scope-list li{display:flex;gap:6px;font-size:10px;line-height:19px}
.scope-list svg{flex:none;margin-top:4px}

/* blog & press */
.blog-item{left:216px;width:286px;display:flex;gap:14px}
.blog-item p{width:220px}
.thumb-round{width:52px;height:52px;border-radius:50%;flex:none;border:2px solid #fff}
.press-item{left:593px;width:388px;display:flex;gap:16px}
.thumb-square{width:61px;height:60px;flex:none;border:2px solid #fff;box-shadow:0 0 0 1px #ccc}
.press-date{font-size:10px;font-weight:700;color:var(--ink)}

/* testimonials */
.carousel-dot{width:21px;height:21px;border-radius:50%;background:#d8d8d8;display:flex;align-items:center;justify-content:center}
.client-name{left:391px;top:1886px;font-size:15px;color:var(--ink)}
.client-place{left:475px;top:1898px;font-size:9px;color:#aaa}

/* footer */
.site-footer{left:0;top:1933px;width:1200px;height:266px;background:var(--footer);color:#fff;font-family:"Arimo",sans-serif}
.footer-col{position:absolute;top:46px}
.footer-col h3{font-size:11px;font-weight:400;letter-spacing:.2px;margin-bottom:20px}
.footer-col p{font-size:9px;line-height:15px;color:#e8e8e8}
.tweet{display:flex;gap:12px;margin-bottom:15px}
.tweet-dot{width:12px;height:12px;border-radius:50%;background:#6a6666;flex:none;margin-top:2px}
.tweet b{font-size:8.5px;line-height:13px;display:block}
.tweet small{font-size:7.5px;color:#8a8585}
.newsletter-field{margin-top:18px;width:233px;height:33px;background:#fff;border-radius:3px;display:flex;align-items:center;justify-content:space-between;padding-left:12px}
.newsletter-field span{font-size:10px;font-style:italic;color:#aaa}
.newsletter-go{width:38px;height:29px;margin-right:2px;background:#d5d5d5;display:flex;align-items:center;justify-content:center;border-radius:2px}
.footer-links{margin-top:16px;font-size:9px}
.footer-links u{text-decoration:underline}
.contact-field{width:228px;height:32px;background:var(--field);border-radius:3px;font-size:9px;display:flex;align-items:center;padding-left:14px;margin-top:8px}

.footer-bottom{left:0;top:2199px;width:1200px;height:40px;background:var(--footer-deep);color:#fff;font-family:"Arimo",sans-serif}
.copyright{position:absolute;left:215px;top:14px;font-size:10px}
.social{position:absolute;left:850px;top:11px;display:flex;gap:16px}
.social span{width:18px;height:18px;border-radius:50%;background:#fff;display:block}
</style>
</head>
<body>

<header class="site-header abs">
  <div class="brand abs"><span class="brand-mark"></span><span class="brand-name">Torvek Legal</span></div>
  <div class="header-phone abs">
    <svg width="16" height="16" viewBox="0 0 24 24" aria-hidden="true"><path fill="#1d1d1d" d="M6.6 10.8a15.1 15.1 0 0 0 6.6 6.6l2.2-2.2a1 1 0 0 1 1-.25 11.4 11.4 0 0 0 3.6.57 1 1 0 0 1 1 1V20a1 1 0 0 1-1 1A17 17 0 0 1 3 4a1 1 0 0 1 1-1h3.5a1 1 0 0 1 1 1c0 1.25.2 2.45.57 3.57a1 1 0 0 1-.25 1z"/></svg>
    0400 318 742
  </div>
</header>

<nav class="main-nav abs">
  <ul>
    <li>HOME</li><li>ABOUT US</li><li>PRACTICE AREAS</li><li>SCOPE OF ADVICE</li><li>LEGAL COSTS</li><li>PRESS</li><li>RECENT CASES</li><li>FAQ</li><li>CONTACT</li><li>SERVICE POLICY</li>
  </ul>
</nav>

<section class="hero abs" role="img" aria-label="Photo of brass scales of justice, law books and a wooden gavel in warm light"></section>
<div class="hero-quote abs">In ultricies pellentesque massa a porta. Aliquam ipsum enim, hendr In eget mi dui, sit amet.In ultricies pellentesque massa a porta</div>
<div class="hero-arrow prev abs"><svg width="18" height="16" viewBox="0 0 18 16" aria-hidden="true"><path d="M9 2 3 8l6 6M15 2 9 8l6 6" fill="none" stroke="#222" stroke-width="2.4"/></svg></div>
<div class="hero-arrow next abs"><svg width="18" height="16" viewBox="0 0 18 16" aria-hidden="true"><path d="M3 2l6 6-6 6M9 2l6 6-6 6" fill="none" stroke="#222" stroke-width="2.4"/></svg></div>

<!-- intro -->
<h1 class="section-title intro-title abs">Criminal Defence Lawyer, Traffic Defence Lawyer &amp; Civil Litigation Lawyer, Perth WA</h1>
<div class="title-rule abs" style="left:213px;top:610px;width:774px"></div>
<div class="photo abs" style="left:213px;top:637px;width:147px;height:117px" role="img" aria-label="Photo of golden scales of justice beside a gavel"></div>
<div class="intro-text abs">
  <p>Torvek Legal is an established law firm practicing in Criminal Law, Traffic Law and Civil Law. We are conveniently located close to the Perth Magistrates Court and District Court. We understand that facing legal proceedings is very daunting and our clients are always saying "we don't know what to expect, we haven't been through anything like this before". We provide easy-to-understand advice and expert assistance to help you navigate complex court procedures. Our legal fees are open and transparent so you know from day one how much your legal defence is going to cost. We service all metropolitan courts as well as providing a visiting service to Karratha and Port Hedland.</p>
  <p style="margin-top:14px">Our office hours are 8:30 - 5:00 pm Monday to Friday but appointments can be made outside of these times.<br>CALL Elias NOW for an obligation FREE assessment of your case on 0400 318 742 or email us.</p>
</div>

<!-- about & scope -->
<section class="band abs" style="top:806px;height:355px"></section>
<h2 class="section-title abs" style="left:213px;top:823px">About Us</h2>
<div class="title-rule abs" style="left:213px;top:852px;width:322px"></div>
<div class="abs" style="left:210px;top:872px;width:360px;height:110px;background:linear-gradient(120deg,#d9642e,#e8824a 40%,#9b3a1c)" role="img" aria-label="Photo of scales, gavel and an open law book on an orange backdrop"></div>
<p class="abs" style="left:213px;top:1002px;width:357px;text-align:justify">Torvek Legal is an established Law firm specialising in Criminal Law, Traffic Law and Civil Law. Dr Elias Torvek is the firm's Legal Practitioner Director. Elias is an experienced Legal Advocate dedicated to protecting you legal rights. In the last two years he has notched up over 2,000 appearances in the Magistrates Court, District Court, Supreme Court and Children's Court.</p>
<div class="more-btn abs" style="left:212px;top:1097px">More</div>

<h2 class="section-title abs" style="left:628px;top:823px">Scope of Advice</h2>
<div class="title-rule abs" style="left:628px;top:852px;width:358px"></div>
<p class="abs" style="left:626px;top:868px;width:362px">At your initial consultation with Elias he will review your case and then advise you on all aspects of your legal situation including:</p>
<ul class="scope-list abs">
  <li><svg width="13" height="11" viewBox="0 0 13 11" aria-hidden="true"><rect x=".5" y="2.5" width="8" height="8" fill="none" stroke="#222"/><path d="M2 6l2.5 2.5L12 1" fill="none" stroke="#222" stroke-width="1.6"/></svg><span>Applicable laws and relevant procedural steps such as what documents to file and when;</span></li>
  <li><svg width="13" height="11" viewBox="0 0 13 11" aria-hidden="true"><rect x=".5" y="2.5" width="8" height="8" fill="none" stroke="#222"/><path d="M2 6l2.5 2.5L12 1" fill="none" stroke="#222" stroke-width="1.6"/></svg><span>Defences available on the facts;</span></li>
  <li><svg width="13" height="11" viewBox="0 0 13 11" aria-hidden="true"><rect x=".5" y="2.5" width="8" height="8" fill="none" stroke="#222"/><path d="M2 6l2.5 2.5L12 1" fill="none" stroke="#222" stroke-width="1.6"/></svg><span>Tactical strategies including whether your case warrants negotiation with police or the Police Prosecution Service, Commonwealth or State DPP;</span></li>
  <li><svg width="13" height="11" viewBox="0 0 13 11" aria-hidden="true"><rect x=".5" y="2.5" width="8" height="8" fill="none" stroke="#222"/><path d="M2 6l2.5 2.5L12 1" fill="none" stroke="#222" stroke-width="1.6"/></svg><span>A range of possible outcomes or sentencing options applicable to your case;</span></li>
  <li><svg width="13" height="11" viewBox="0 0 13 11" aria-hidden="true"><rect x=".5" y="2.5" width="8" height="8" fill="none" stroke="#222"/><path d="M2 6l2.5 2.5L12 1" fill="none" stroke="#222" stroke-width="1.6"/></svg><span>Legal costs and estimated time frame to finalise your case;</span></li>
</ul>
<div class="more-btn abs" style="left:621px;top:1094px">More</div>

<!-- legal costs -->
<h2 class="section-title abs" style="left:213px;top:1188px">Legal Costs</h2>
<div class="title-rule abs" style="left:213px;top:1219px;width:774px"></div>
<div class="abs" style="left:213px;top:1248px;width:545px">
  <p>Our Legal Cost Structure is OPEN and TRANSPARENT there are no hidden costs.</p>
  <p style="margin-top:15px">Our legal advice is valuable but we ensure that our legal costs are competitive with other firms in the profession.</p>
  <p style="margin-top:15px">When you first telephone us, we will provide you with an obligation FREE assessment of your case. If you want to know more then an appointment will be made for your initial consultation for you to provide us with your instructions and for you to receive our preliminary advice.</p>
</div>
<div class="photo abs" style="left:780px;top:1245px;width:172px;height:103px;background:linear-gradient(135deg,#4a2e1e,#1a1a22 60%,#3a2616)" role="img" aria-label="Photo of a lawyer in a suit holding books in front of a library shelf"></div>

<!-- blog & press -->
<section class="band abs" style="top:1403px;height:298px"></section>
<h2 class="section-title abs" style="left:221px;top:1428px">Blog</h2>
<div class="blog-item abs" style="top:1470px">
  <div class="thumb-round" style="background:linear-gradient(135deg,#f1e2d3,#b98b64)" role="img" aria-label="Thumbnail photo of a hand signing a document"></div>
  <p>In ultricies pellentesque massa a porta. Aliquam ipsum enim, hendrerit ut porta nec. ullamcorper et nulla. In eget mi dui, sit amet.</p>
</div>
<div class="title-rule abs" style="left:216px;top:1530px;width:280px;background:#cfcfcf"></div>
<div class="blog-item abs" style="top:1542px">
  <div class="thumb-round" style="background:linear-gradient(135deg,#f3f3f3,#a9a296)" role="img" aria-label="Thumbnail photo of scales of justice"></div>
  <p>In ultricies pellentesque massa a porta. Aliquam ipsum enim, hendrerit ut porta nec. ullamcorper et nulla. In eget mi dui, sit amet.</p>
</div>
<div class="title-rule abs" style="left:216px;top:1606px;width:280px;background:#cfcfcf"></div>
<div class="blog-item abs" style="top:1619px">
  <div class="thumb-round" style="background:linear-gradient(135deg,#c58a32,#3a2410)" role="img" aria-label="Thumbnail photo of a gavel and books"></div>
  <p>In ultricies pellentesque massa a porta. Aliquam ipsum enim, hendrerit ut porta nec. ullamcorper et nulla. In eget mi dui, sit amet.</p>
</div>

<h2 class="section-title abs" style="left:594px;top:1428px">Press</h2>
<div class="press-item abs" style="top:1476px">
  <div class="thumb-square" style="background:linear-gradient(135deg,#3b4a5c,#6b2a1e)" role="img" aria-label="Thumbnail photo of law books on a shelf"></div>
  <div><div class="press-date">23-04-2014</div><p>Torvek Legal is an established Law firm specialising in Criminal Law, Traffic Law and Civil Law. Dr Elias Torvek is the firm's Legal Practitioner Director. Elias is an experienced Legal Advocate dedicated to protecting you legal rights.</p></div>
</div>
<div class="press-item abs" style="top:1572px">
  <div class="thumb-square" style="background:linear-gradient(135deg,#f0d6a8,#b4652a)" role="img" aria-label="Thumbnail photo of a wooden gavel"></div>
  <div><div class="press-date">21-04-2014</div><p>Torvek Legal is an established Law firm specialising in Criminal Law, Traffic Law and Civil Law. Dr Elias Torvek is the firm's Legal Practitioner Director. Elias is an experienced Legal Advocate dedicated to protecting you legal rights.</p></div>
</div>

<!-- testimonials -->
<h2 class="section-title abs" style="left:222px;top:1727px">Testimonials</h2>
<div class="carousel-dot abs" style="left:214px;top:1817px"><svg width="8" height="10" viewBox="0 0 8 10" aria-hidden="true"><path d="M6 1 2 5l4 4" fill="none" stroke="#fff" stroke-width="1.8"/></svg></div>
<div class="carousel-dot abs" style="left:960px;top:1817px"><svg width="8" height="10" viewBox="0 0 8 10" aria-hidden="true"><path d="M2 1l4 4-4 4" fill="none" stroke="#fff" stroke-width="1.8"/></svg></div>
<div class="abs" style="left:284px;top:1781px;width:89px;height:80px;background:linear-gradient(135deg,#f2f2f2,#9a9a9a)" role="img" aria-label="Photo of a client working at a laptop"></div>
<p class="abs" style="left:391px;top:1777px;width:516px;text-align:justify;line-height:17.5px">Pellentesque habitant morbi tristique senectus et netus et malesuada fames ac turpis egestas. Vestibulum scelerisque dignissim massa, sed gravida nisi sollicitudin vel. Sed nec erat feugiat orci hendrerit ultricies et sit amet lectus. Sed eget tellus sapien. Proin vel mi nibh, id ultrices metus. Donec bibendum dolor at ante lacinia blandit. Vivamus rhoncus mattis sem ut hendrerit. sollicitudin vel. Sed nec erat feugiat orci hendrerit ultricies et sit amet lectus. Sed eget tellus sapien. Proin vel mi nibh, id ultrices metus. Donec bibendum dolor at ante lacinia blandit.</p>
<div class="client-name abs">Client Name</div>
<div class="client-place abs">United States</div>

<!-- footer -->
<footer class="site-footer abs">
  <div class="footer-col" style="left:218px;width:230px">
    <h3 style="margin-left:24px">RECENT TWEETS</h3>
    <div class="tweet"><span class="tweet-dot"></span><div><b>Phasellus euismod luctus augue at pellentesque.<br>Curabitur rutrum vehicula est at dignissim.</b><small>3 days ago</small></div></div>
    <div class="tweet"><span class="tweet-dot"></span><div><b>Phasellus euismod luctus augue at pellentesque.</b><small>6 days ago</small></div></div>
    <div class="tweet"><span class="tweet-dot"></span><div><b>Phasellus euismod luctus augue at pellentesque.</b><small>10 days ago</small></div></div>
  </div>
  <div class="footer-col" style="left:484px;width:240px">
    <h3>SUBSCRIBE TO OUR NEWSLETTER</h3>
    <p>Enter your email address below to subscribe. You will receive our newsletter once a week.</p>
    <div class="newsletter-field"><span>enter your email address</span><div class="newsletter-go"><svg width="7" height="10" viewBox="0 0 7 10" aria-hidden="true"><path d="M1 1l4 4-4 4" fill="none" stroke="#222" stroke-width="2"/></svg></div></div>
    <div class="footer-links"><u>Terms of Use</u> &nbsp;|&nbsp; <u>Privacy Policy</u></div>
  </div>
  <div class="footer-col" style="left:757px;width:240px">
    <h3>LET'S KEEP IN TOUCH</h3>
    <p>You can contact us by using the contact information below or by sending us a message via <u>our contact form</u>.</p>
    <div class="contact-field" style="margin-top:12px">Street Name, Adress,</div>
    <div class="contact-field">Phone: +1 (310) 555 0142</div>
    <div class="contact-field">Email: info@torveklegal.com</div>
  </div>
</footer>
<div class="footer-bottom abs">
  <div class="copyright">Copy right © 2014 Torvek Legal . All rights reserved.</div>
  <div class="social"><span aria-label="Social profile link 1"></span><span aria-label="Social profile link 2"></span><span aria-label="Social profile link 3"></span><span aria-label="Social profile link 4"></span></div>
</div>

</body>
</html>
```